Trade Show Booth Design

Graphic design for main wall of tradeshow booth (back wall)

Graphic design for standing banner that will be positioned at front of booth

Design is showcasing our Logistics Company strengths and services

I am including a general graphic design to be used as direction for the design development.

I am including the text to be used for descriptions of our company's strengths and services

I am including the company logo and images to be used in the designs

```html
<!DOCTYPE html>
<html lang="en">
<head>
<meta charset="utf-8">
<title>Meridian Freight America – Roll-up Banner</title>
<link href="https://fonts.googleapis.com/css2?family=Anton&family=Arimo:wght@400;700&family=Hind:wght@500;600&family=Montserrat:wght@700&display=swap" rel="stylesheet">
<style>
  :root {
    --brand-red: #d91a47;
    --brand-red-deep: #c8133e;
    --ink: #0d0d0d;
    --paper: #ffffff;
    --stage: #a6a4a0;
    --mist-top: #ecebe8;
    --mist-bottom: #f6f5f3;
  }
  * { margin: 0; padding: 0; box-sizing: border-box; }
  html, body {
    width: 1200px; height: 1200px; overflow: hidden;
    background: var(--stage);
  }
  .banner {
    position: absolute;
    left: 314px; top: 30px;
    width: 714px; height: 1426px;
    transform: scale(0.8);
    transform-origin: top left;
    overflow: hidden;
    background: var(--mist-bottom);
  }
  .banner__art { position: absolute; inset: 0; }

  .brand {
    position: absolute; left: 28px; top: 26px;
    display: flex; align-items: center; gap: 12px;
    font-family: "Hind", sans-serif; font-weight: 600;
    font-size: 21px; color: var(--ink); letter-spacing: 0.2px;
  }
  .brand__dot {
    width: 30px; height: 30px; border-radius: 50%;
    background: var(--brand-red);
  }

  .headline {
    position: absolute; left: 0; width: 100%; top: 556px;
    text-align: center;
    font-family: "Anton", sans-serif; font-size: 54px; line-height: 58px;
    color: var(--ink); text-transform: uppercase;
  }
  .headline__accent { color: var(--brand-red); }

  .section-pill {
    position: absolute; left: 58px; top: 681px;
    width: 597px; height: 38px; border-radius: 6px;
    background: var(--brand-red);
    color: var(--paper);
    font-family: "Arimo", sans-serif; font-weight: 700;
    font-size: 31px; line-height: 38px; text-align: center;
  }

  .service {
    position: absolute; width: 317px; height: 247px;
    display: flex; flex-direction: column;
  }
  .service--transport { left: 28px; top: 738px; }
  .service--warehouse { left: 367px; top: 738px; }
  .service--heavy { left: 28px; top: 1003px; }
  .service--customs { left: 367px; top: 1003px; }

  .service__photo { height: 171px; }
  .service--transport .service__photo { background: linear-gradient(160deg, #8fb7cf 0%, #c9a760 45%, #c54a3a 70%, #6d6a66 100%); }
  .service--warehouse .service__photo { background: linear-gradient(180deg, #d39a5c 0%, #c9915a 40%, #9a8c7e 75%, #d7d2cb 100%); }
  .service--heavy .service__photo { background: linear-gradient(180deg, #2f6fd0 0%, #6aa0e6 35%, #a08d73 70%, #5b4f45 100%); }
  .service--customs .service__photo { background: linear-gradient(135deg, #2a3a5a 0%, #6f86a8 45%, #c8ccd2 70%, #2c3446 100%); }

  .service__caption {
    flex: 1; background: var(--brand-red); color: var(--paper);
    text-align: center;
    display: flex; flex-direction: column; justify-content: center;
    padding: 0 6px;
  }
  .service__title {
    font-family: "Montserrat", sans-serif; font-weight: 700;
    font-size: 15px; line-height: 18px; text-transform: uppercase;
  }
  .service__title--small { font-size: 13px; line-height: 17px; }
  .service__detail {
    font-family: "Hind", sans-serif; font-weight: 500;
    font-size: 15px; line-height: 20px; margin-top: 2px;
  }

  .cta {
    position: absolute; left: 28px; top: 1289px;
    width: 392px; height: 49px; border-radius: 6px;
    background: var(--ink); color: var(--paper);
    font-family: "Arimo", sans-serif; font-size: 20px;
    line-height: 49px; text-align: center;
  }

  .footer-web {
    position: absolute; left: 28px; top: 1385px;
    display: flex; align-items: center; gap: 12px;
    font-family: "Arimo", sans-serif; font-weight: 700;
    font-size: 17px; color: var(--paper);
  }
  .footer-brand {
    position: absolute; right: 28px; top: 1346px;
    font-family: "Hind", sans-serif; font-weight: 600;
    font-size: 17px; color: var(--paper); text-align: right; line-height: 20px;
  }
</style>
</head>
<body>
<main class="banner">
  <svg class="banner__art" width="714" height="1426" viewBox="0 0 714 1426" aria-hidden="false">
    <defs>
      <linearGradient id="hero-tone" x1="0" y1="0" x2="1" y2="1">
        <stop offset="0" stop-color="#c9d6e4"/>
        <stop offset="0.35" stop-color="#c58a6a"/>
        <stop offset="0.6" stop-color="#e5733c"/>
        <stop offset="1" stop-color="#1c2f6a"/>
      </linearGradient>
      <linearGradient id="mist-tone" x1="0" y1="0" x2="0" y2="1">
        <stop offset="0" stop-color="#e6e4e0"/>
        <stop offset="0.5" stop-color="#efeeeb"/>
        <stop offset="1" stop-color="#f7f6f4"/>
      </linearGradient>
    </defs>
    <rect x="0" y="0" width="714" height="90" fill="#f3f5f8"/>
    <rect x="0" y="90" width="714" height="420" fill="url(#hero-tone)" role="img" aria-label="Photo collage of a container ship at port cranes, a cargo plane, a glowing globe and trucks on a highway"/>
    <path d="M0,470 C220,418 480,460 714,506 L714,1426 L0,1426 Z" fill="url(#mist-tone)" role="img" aria-label="Faded photo of a warehouse interior with tall racking"/>
    <path d="M0,250 C170,330 420,440 714,482 L714,506 C480,460 220,418 0,470 Z" fill="var(--brand-red-deep)"/>
    <path d="M714,1215 C660,1330 520,1370 320,1372 L0,1372 L0,1426 L714,1426 Z" fill="var(--brand-red-deep)"/>
    <g transform="translate(40,1398)" fill="none" stroke="#ffffff" stroke-width="2">
      <circle r="10"/>
      <ellipse rx="4.5" ry="10"/>
      <line x1="-10" y1="0" x2="10" y2="0"/>
    </g>
  </svg>

  <div class="brand"><span class="brand__dot"></span>MERIDIAN FREIGHT AMERICA</div>

  <h1 class="headline">Your <span class="headline__accent">Global Partner</span> for<br>Turbomachinery Logistics</h1>

  <div class="section-pill">OUR STRENGTHS AND SERVICES</div>

  <section class="service service--transport">
    <div class="service__photo" role="img" aria-label="Red truck with trailer under port cranes and a forklift"></div>
    <div class="service__caption">
      <p class="service__title">NVOCC &amp; Global Supply<br>Chain Management</p>
      <p class="service__detail">International/Domestic Transportation</p>
    </div>
  </section>

  <section class="service service--warehouse">
    <div class="service__photo" role="img" aria-label="Warehouse aisle between tall pallet racks"></div>
    <div class="service__caption">
      <p class="service__title">3PL and Foreign<br>Trade Zone (FTZ)</p>
      <p class="service__detail">Warehousing</p>
    </div>
  </section>

  <section class="service service--heavy">
    <div class="service__photo" role="img" aria-label="Gantry lift loading heavy turbine equipment onto a trailer"></div>
    <div class="service__caption">
      <p class="service__title">Heavy Haul, Out of Gauge,<br>Project Management</p>
      <p class="service__detail">Project Logistics</p>
    </div>
  </section>

  <section class="service service--customs">
    <div class="service__photo" role="img" aria-label="Digital customs interface with circular icons over a business background"></div>
    <div class="service__caption">
      <p class="service__title service__title--small">Optimize your import export<br>business with our in-house customs<br>&amp; trade compliance</p>
      <p class="service__detail">Import, Export &amp; Trade compliance</p>
    </div>
  </section>

  <div class="cta">CONTACT US FOR A FREE QUOTE</div>

  <div class="footer-web"><span style="width:20px"></span>WWW.MERIDIANFREIGHTLOGISTICS.COM</div>
  <div class="footer-brand">MERIDIAN<br>FREIGHT</div>
</main>
</body>
</html>
```